Business Card Design needed Have Logo Files

Hello, I am in need of a business card design.

Company Name: Quartz Traders

Company Address:
2714 E. Palmer Ave
Suite 482B
North Las Vegas, Nevada 97415

I think the colors blue, grey, silver (metallic), white, and black are good choices to go with for coloring.

The Owen Pratt and the Copper Sheet are my favorites from the examples so far. Love the bring and edgy blues.

Photo's I have added are designs that I like. I'll also be adding source files.

Logo Source documents have been added.

Project Deadline Extended
Reason: Father passed away and had to take care of his affairs, back in business now.

Need front and back. Try to give it a backside that has a wow factor to it. I've changed the color spectrum to blue, black, purple, and pink for the front side. Think of it as 90% blue and black, 7% purple, 3 % pink when it comes to thinking of ratios of how much of each color i'd like to see on the card. Backside you can use any of those 4 colors as much as you'd like to give it memorable.

Industry/Entity Type

Business

Colors
0492cd
33a6d7
0355a3
3176b5
ffffff
aaaaaa
cbcbcb
9d9d9d
5c5c5c

Requirements
Must have
• Name
Company Address
Work Number
Mobile Number

Doublesided.
Rounded edges

```html
<!DOCTYPE html>
<html lang="en">
<head>
<meta charset="utf-8">
<title>Quartz Traders – Business Card</title>
<link href="https://fonts.googleapis.com/css2?family=Lato:wght@400;700;900&display=swap" rel="stylesheet">
<style>
  :root {
    --stage: #2a2a2c;
    --blue-deep: #0355a3;
    --blue-mid: #3176b5;
    --blue-bright: #0492cd;
    --blue-light: #33a6d7;
    --white: #ffffff;
    --silver: #cbcbcb;
    --ink: #1e1e1e;
  }
  * { margin: 0; padding: 0; box-sizing: border-box; }
  html, body { width: 1200px; height: 800px; overflow: hidden; }
  body {
    background: var(--stage);
    font-family: "Lato", Arial, sans-serif;
    position: relative;
  }
  .card {
    position: absolute;
    top: 255px;
    width: 525px;
    height: 300px;
    border-radius: 22px;
    overflow: hidden;
  }
  .card-back {
    left: 50px;
    background: linear-gradient(135deg, var(--blue-mid) 0%, var(--blue-deep) 70%);
  }
  .card-front { left: 625px; background: var(--white); }

  .brand {
    position: absolute;
    display: flex;
    align-items: center;
    gap: 12px;
  }
  .brand-dot {
    width: 34px; height: 34px;
    border-radius: 50%;
    background: var(--blue-light);
  }
  .brand-name {
    font-weight: 900;
    font-size: 30px;
    letter-spacing: 1px;
    color: var(--silver);
    text-transform: uppercase;
  }
  .card-back .brand { left: 50%; top: 50%; transform: translate(-50%, -50%); }
  .card-front .brand { left: 34px; top: 118px; }
  .card-front .brand-name { font-size: 26px; }

  .front-wave { position: absolute; inset: 0; width: 100%; height: 100%; }

  .person {
    position: absolute;
    right: 24px; top: 18px;
    text-align: right;
    color: var(--white);
  }
  .person-name { font-weight: 700; font-size: 22px; letter-spacing: .5px; }
  .person-title { font-size: 15px; }

  .contact {
    position: absolute;
    right: 24px;
    text-align: right;
    color: var(--ink);
    font-size: 15px;
    line-height: 1.3;
  }
  .contact-phones { top: 100px; }
  .contact-address { top: 172px; }
  .contact-line { display: flex; justify-content: flex-end; align-items: center; gap: 6px; }
  .icon { width: 12px; height: 12px; fill: var(--blue-bright); }
</style>
</head>
<body>

  <section class="card card-back">
    <div class="brand">
      <span class="brand-dot"></span>
      <span class="brand-name">Quartz Traders</span>
    </div>
  </section>

  <section class="card card-front">
    <svg class="front-wave" viewBox="0 0 525 300" preserveAspectRatio="none" aria-hidden="true">
      <defs>
        <linearGradient id="waveBlue" x1="0" y1="0" x2="1" y2="1">
          <stop offset="0" stop-color="#3176b5"/>
          <stop offset="0.6" stop-color="#0355a3"/>
          <stop offset="1" stop-color="#0492cd"/>
        </linearGradient>
        <linearGradient id="waveGlow" x1="0" y1="0" x2="1" y2="0">
          <stop offset="0" stop-color="#33a6d7"/>
          <stop offset="1" stop-color="#ffffff"/>
        </linearGradient>
      </defs>
      <path d="M0 0 H525 V62 C430 70 380 110 350 170 C320 235 250 265 0 270 Z" fill="url(#waveBlue)"/>
      <path d="M525 62 C430 70 380 110 350 170 C320 235 250 265 0 270 V285 C270 280 340 245 368 180 C395 118 440 80 525 72 Z" fill="url(#waveGlow)" opacity="0.75"/>
    </svg>

    <div class="person">
      <div class="person-name">Dana Keller</div>
      <div class="person-title">president</div>
    </div>

    <div class="brand">
      <span class="brand-dot"></span>
      <span class="brand-name">Quartz Traders</span>
    </div>

    <div class="contact contact-phones">
      <div class="contact-line">482 617 3905
        <svg class="icon" viewBox="0 0 12 12"><path d="M2 1h2.5l1 3-1.5 1a6 6 0 0 0 3 3l1-1.5 3 1V10a1 1 0 0 1-1 1A9 9 0 0 1 1 2a1 1 0 0 1 1-1z"/></svg>
      </div>
      <div class="contact-line">714 308 2956
        <svg class="icon" viewBox="0 0 12 12"><rect x="3" y="0.5" width="6" height="11" rx="1.2" fill="none" stroke="#0492cd" stroke-width="1.2"/></svg>
      </div>
    </div>

    <div class="contact contact-address">
      <div class="contact-line">2714 E. Palmer Ave
        <svg class="icon" viewBox="0 0 12 12"><path d="M6 0a4 4 0 0 0-4 4c0 3 4 8 4 8s4-5 4-8a4 4 0 0 0-4-4zm0 5.5A1.5 1.5 0 1 1 6 2.5a1.5 1.5 0 0 1 0 3z"/></svg>
      </div>
      <div class="contact-line">Suite 482B</div>
      <div class="contact-line">North Las Vegas, Nevada 97415</div>
    </div>
  </section>

</body>
</html>
```